Linden Medical - Flyer

We are a full service pharmacy that specializes in diabetic testing and medications. We research the patient's insurance to maximize their insurance benefit and then deliver the medications monthly directly to the patient's doorstep, for free! We save the patient, time and money every month.
We would love a flyer that we can distribute to Doctor's offices and patients that sum up our pharmacy. Emphasis on saving money, time, and getting the best quality supplies by maximizing their insurance. We want it to be eye catching, clean, and professional.
You can use our logo or feel free to make your own design.
Updates
Target Market(s)
diabetic patients wanting to save money
Industry/Entity Type
Insurance
Look and feel
Each slider illustrates characteristics of the customer's brand and the style your logo design should communicate.

```html
<!DOCTYPE html>
<html lang="en">
<head>
<meta charset="utf-8">
<title>Linden Medical – Flyer</title>
<link rel="stylesheet" href="https://fonts.googleapis.com/css2?family=Open+Sans:ital,wght@0,400;0,700;1,700&family=Anton&display=swap">
<style>
  :root {
    --ink: #111111;
    --brand-grey: #4a4a4a;
    --brand-green: #8cc63f;
    --paper: #ffffff;
    --cream: #fdf5c4;
    --peach: #fbd69a;
    --apricot: #f9b97a;
    --badge: #f7941d;
    --photo-warm: #b98a66;
    --photo-cool: #7d7f86;
    --photo-red: #a23a3a;
  }
  * { margin: 0; padding: 0; box-sizing: border-box; }
  html, body { width: 1200px; height: 2540px; overflow: hidden; background: var(--paper); }
  .flyer {
    position: relative; width: 1200px; height: 2540px; overflow: hidden;
    font-family: "Open Sans", Arial, sans-serif; color: var(--ink);
    background: linear-gradient(172deg, var(--paper) 0%, var(--paper) 13%, var(--cream) 30%, var(--peach) 60%, var(--apricot) 78%);
  }
  .brand {
    position: absolute; top: 110px; left: 0; width: 1200px;
    display: flex; align-items: center; justify-content: center; gap: 34px;
  }
  .brand-dot { width: 120px; height: 120px; border-radius: 50%; background: var(--brand-green); }
  .brand-name { font-size: 92px; font-weight: 400; color: var(--brand-grey); letter-spacing: 1px; line-height: 1; }
  .content { position: absolute; left: 85px; top: 366px; width: 1100px; }
  .title { font-size: 43px; font-weight: 700; font-style: italic; line-height: 60px; }
  .body-copy { font-size: 47px; line-height: 61px; white-space: nowrap; }
  .services { list-style: none; margin: 10px 0 6px 0; }
  .services li { position: relative; padding-left: 80px; font-size: 47px; line-height: 74px; }
  .services li::before {
    content: ""; position: absolute; left: 47px; top: 32px;
    width: 14px; height: 14px; border-radius: 50%; background: var(--ink);
  }
  .contact { position: absolute; left: 85px; top: 1418px; }
  .contact-heading { font-size: 45px; font-weight: 700; line-height: 68px; }
  .contact-line { font-size: 47px; line-height: 62px; }
  .saving-badge {
    position: absolute; left: 715px; top: 1346px; width: 398px; height: 398px;
    border-radius: 50%; background: var(--badge);
    display: flex; flex-direction: column; align-items: center; justify-content: center;
    font-family: "Anton", Impact, sans-serif; color: var(--ink); text-align: center;
  }
  .saving-badge .lead { font-size: 46px; line-height: 50px; }
  .saving-badge .figure { font-size: 132px; line-height: 126px; }
  .saving-badge .word { font-size: 66px; line-height: 70px; }
  .saving-badge .note { font-size: 26px; line-height: 32px; }
  .photo-band { position: absolute; left: 0; top: 1720px; width: 1200px; height: 820px; }
</style>
</head>
<body>
<div class="flyer">
  <header class="brand">
    <span class="brand-dot"></span>
    <span class="brand-name">Linden Medical</span>
  </header>

  <main class="content">
    <h2 class="title">Your Diabetic Pharmacy</h2>
    <p class="body-copy">Linden Medical is a full service pharmacy<br>specializing in diabetic testing supplies<br>and medications. We research your plan<br>to maximize your insurance benefit and<br>get you the best quality supplies for less</p>
    <ul class="services">
      <li>Diabetic testing</li>
      <li>Medications</li>
      <li>Insurance review</li>
      <li>Free delivery</li>
      <li>Monthly refills</li>
    </ul>
    <p class="body-copy">Every month we deliver your medications<br>straight to your doorstep, free of charge,<br>saving you time and money every single<br>month</p>
  </main>

  <section class="contact">
    <h3 class="contact-heading">More Information</h3>
    <p class="contact-line">08 8200 3000 4100</p>
    <p class="contact-line">info@lindenmedical.com</p>
    <p class="contact-line">www.lindenmedical.com</p>
  </section>

  <div class="saving-badge">
    <span class="lead">up to</span>
    <span class="figure">10%</span>
    <span class="word">saving</span>
    <span class="note">compared to retail</span>
  </div>

  <svg class="photo-band" viewBox="0 0 1200 820" width="1200" height="820">
    <defs>
      <linearGradient id="photo-tone" x1="0" y1="0" x2="1" y2="1">
        <stop offset="0" stop-color="var(--photo-warm)"/>
        <stop offset="0.5" stop-color="var(--photo-cool)"/>
        <stop offset="1" stop-color="var(--photo-red)"/>
      </linearGradient>
    </defs>
    <polygon points="0,192 1200,30 1200,76 0,248" fill="var(--paper)"/>
    <polygon points="0,248 1200,76 1200,820 0,820" fill="url(#photo-tone)" role="img" aria-label="Photo: a smiling delivery driver handing a parcel to an older woman at her front door"/>
  </svg>
</div>
</body>
</html>
```